Looking for awesome business card design with attached existing logo

We are a water, mold, and fire damage restoration company called "Torvane Seco" Looking for an awesome business card that is edgy yet professional and unique. Show me what you got!

```html
<!DOCTYPE html>
<html lang="en">
<head>
<meta charset="UTF-8">
<title>Torvane Seco – Business Card</title>
<link href="https://fonts.googleapis.com/css2?family=Poppins:wght@400;500;700&display=swap" rel="stylesheet">
<style>
  :root {
    --teal: #2d4a55;
    --gold: #d4951f;
    --white: #ffffff;
    --ink: #1e1e1e;
    --rule: #9a9a9a;
    --stage: #b8b8b8;
  }
  * { margin: 0; padding: 0; box-sizing: border-box; }
  html, body { width: 1200px; height: 1200px; overflow: hidden; }
  body {
    background: var(--stage);
    font-family: "Poppins", sans-serif;
    display: flex;
    align-items: center;
    justify-content: center;
    gap: 30px;
  }
  .card {
    width: 369px;
    height: 594px;
    position: relative;
    display: flex;
    flex-direction: column;
    align-items: center;
  }
  .card-front {
    background: linear-gradient(180deg, #2d4a55 0%, #2e4b56 60%, #2d4a55 100%);
  }
  .card-back { background: var(--white); }

  .brand {
    display: flex;
    align-items: center;
    gap: 10px;
    font-weight: 700;
    font-size: 34px;
    letter-spacing: 1px;
    line-height: 1;
  }
  .brand-dot { width: 14px; height: 14px; border-radius: 50%; background: var(--gold); }
  .card-front .brand { color: var(--white); position: absolute; top: 460px; }
  .card-back .brand { color: var(--teal); margin-top: 215px; }

  .person { margin-top: 120px; text-align: center; }
  .person-name { font-weight: 700; font-size: 24px; color: var(--teal); letter-spacing: 0.5px; line-height: 1.1; }
  .person-role { font-weight: 400; font-size: 15px; color: var(--gold); letter-spacing: 0.3px; }

  .icon-row {
    display: flex; align-items: center; gap: 5px; margin-top: 12px;
  }
  .icon-row .rule { width: 52px; height: 1px; background: var(--rule); margin: 0 4px; }
  .icon-box {
    width: 25px; height: 25px; border-radius: 3px; background: var(--teal);
    display: flex; align-items: center; justify-content: center;
  }
  .contact { margin-top: 8px; text-align: center; font-size: 16px; color: var(--ink); line-height: 21px; }
  .divider { width: 195px; height: 1px; background: var(--rule); margin-top: 13px; }
  .address { margin-top: 13px; text-align: center; font-size: 16px; color: var(--ink); line-height: 21px; }
</style>
</head>
<body>
  <section class="card card-front">
    <div class="brand"><span class="brand-dot"></span>TORVANE SECO</div>
  </section>

  <section class="card card-back">
    <div class="brand"><span class="brand-dot"></span>TORVANE SECO</div>

    <div class="person">
      <div class="person-name">MARCUS HALE</div>
      <div class="person-role">MANAGING DIRECTOR</div>
    </div>

    <div class="icon-row">
      <span class="rule"></span>
      <span class="icon-box" aria-label="Phone">
        <svg width="15" height="15" viewBox="0 0 16 16"><path d="M2 6c0-2 2-3 6-3s6 1 6 3l-3 1-1-2H6L5 7 2 6z M4 8h8l1 5H3z" fill="#fff"/></svg>
      </span>
      <span class="icon-box" aria-label="Email">
        <svg width="15" height="15" viewBox="0 0 16 16"><rect x="1.5" y="3.5" width="13" height="9" fill="none" stroke="#fff"/><path d="M1.5 3.5 8 9l6.5-5.5" fill="none" stroke="#fff"/></svg>
      </span>
      <span class="icon-box" aria-label="Website">
        <svg width="15" height="15" viewBox="0 0 16 16"><circle cx="8" cy="8" r="6.5" fill="#fff"/><path d="M5 4c2 1 1 3 3 3s0 3 2 4M10 3c-1 2 2 2 3 3" fill="none" stroke="#2d4a55" stroke-width="1.3"/></svg>
      </span>
      <span class="rule"></span>
    </div>

    <div class="contact">
      <div>055-318 640 217</div>
      <div>INFO@TORVANESECO.COM</div>
      <div>WWW.TORVANESECO.COM</div>
    </div>

    <div class="divider"></div>

    <div class="address">
      <div>87, HARBOR MILL ROAD</div>
      <div>30918, EASTLAND</div>
    </div>
  </section>
</body>
</html>
```